Golden Era Hollywood Movie Poster Design for a Wedding Invitation

We're looking for a movie poster designed along the lines of the styles of posters in the included "posters" file. We're thinking the "title" of the "movie" should be "The Wedding of the Year". This will be for a wedding invitation to the wedding of "Marla Vostenkiew" and "Daniel Ferroway", so their names should be featured as the "stars" of the movie. The wedding will take place at Cal Brindle Studios in Hollywood, so you can put on the poster "Presented by Cal Brindle Studios". The other uploaded files are photos of the bride and groom. You don't need to use any of the poses in those photos - we'd like to have a pose that's along the lines of the examples in the "posters" file - but I included the photos of the bride and groom as references to help you make the final poster look like them (but in the style of an old Hollywood movie poster). Make them look beautiful and glamorous like stars in a movie from Hollywood's golden era. :)

Project Deadline Extended
Reason: The designs we've received so far aren't quite giving exactly the old-Hollywood feel we're looking for, so we're giving one 5-day extension to see additional designs.

```html
<!DOCTYPE html>
<html lang="en">
<head>
<meta charset="utf-8">
<title>The Wedding of the Year</title>
<link rel="stylesheet" href="https://fonts.googleapis.com/css2?family=League+Gothic&family=Oswald:wght@300;400;500&family=Cormorant+Garamond:ital,wght@1,400&display=swap">
<style>
  :root {
    --backdrop: #e9e7e4;
    --poster-black: #000000;
    --title-red: #ee1c1c;
    --ink-white: #ffffff;
    --art-light: #f4f4f4;
    --art-mid: #9a9a9a;
  }
  * { margin: 0; padding: 0; box-sizing: border-box; }
  html, body {
    width: 1200px;
    height: 1148px;
    overflow: hidden;
    background: var(--backdrop);
  }
  .poster {
    position: absolute;
    left: 250px;
    top: 24px;
    width: 700px;
    height: 1100px;
    background: var(--poster-black);
    color: var(--ink-white);
    text-align: center;
  }
  .presenter {
    position: absolute;
    top: 30px;
    left: 0;
    right: 0;
  }
  .presenter-label {
    display: block;
    font-family: "Oswald", sans-serif;
    font-weight: 400;
    font-size: 12px;
    letter-spacing: 7px;
    color: var(--title-red);
    text-transform: uppercase;
  }
  .presenter-name {
    display: block;
    margin-top: 2px;
    font-family: "Oswald", sans-serif;
    font-weight: 500;
    font-size: 28px;
    text-transform: uppercase;
  }
  .couple-art {
    position: absolute;
    left: 40px;
    top: 130px;
    width: 640px;
    height: 520px;
  }
  .title {
    position: absolute;
    top: 600px;
    left: 0;
    right: 0;
    font-weight: normal;
  }
  .title-article {
    display: block;
    font-family: "Cormorant Garamond", serif;
    font-style: italic;
    font-weight: 400;
    font-size: 96px;
    line-height: 0.9;
  }
  .title-main {
    display: block;
    font-family: "League Gothic", sans-serif;
    font-size: 240px;
    line-height: 0.82;
    color: var(--title-red);
    text-transform: uppercase;
  }
  .title-sub {
    display: block;
    margin-top: 6px;
    font-family: "League Gothic", sans-serif;
    font-size: 72px;
    line-height: 0.9;
    text-transform: uppercase;
  }
  .billing {
    position: absolute;
    top: 958px;
    left: 0;
    right: 0;
  }
  .billing-label {
    display: block;
    font-family: "Oswald", sans-serif;
    font-weight: 300;
    font-size: 22px;
    letter-spacing: 8px;
    line-height: 1;
    text-transform: uppercase;
  }
  .billing-names {
    display: block;
    margin-top: 12px;
    font-family: "League Gothic", sans-serif;
    font-size: 22px;
    text-transform: uppercase;
  }
</style>
</head>
<body>
  <main class="poster">
    <header class="presenter">
      <span class="presenter-label">Presented by</span>
      <span class="presenter-name">Cal Brindle Studios</span>
    </header>

    <svg class="couple-art" viewBox="0 0 640 520" role="img" aria-label="High-contrast black and white illustration of the groom tipping his cap while the bride kisses his cheek">
      <defs>
        <radialGradient id="artTone" cx="50%" cy="42%" r="55%">
          <stop offset="0%" stop-color="var(--art-light)"/>
          <stop offset="55%" stop-color="var(--art-mid)"/>
          <stop offset="100%" stop-color="var(--poster-black)"/>
        </radialGradient>
      </defs>
      <rect width="640" height="520" fill="url(#artTone)"/>
    </svg>

    <h1 class="title">
      <span class="title-article">The</span>
      <span class="title-main">Wedding</span>
      <span class="title-sub">of the Year</span>
    </h1>

    <footer class="billing">
      <span class="billing-label">Featuring</span>
      <span class="billing-names">Marla Vostenkiew and Daniel Ferroway</span>
    </footer>
  </main>
</body>
</html>
```